Web Design for Harbor Link Guild

We need a web design for Harbor Link Guild. You can see more details about the kind of business that it deals with in this link: http://harborlinkguild.ae/. The concept of the site is similar to http://www.travimo.com/ and we are looking for a homepage design also similar to it.
The top navigation should have:
1) directory
2) articles
3) deals
4) forums
5) log in/register page.
It should also have a video, a slider, map & text as well as a call to action to a "why register page".
As part of the footer it should include:
1) about HLG
2) contact HGL
3) terms & conditions
4) privacy
The color palette for the site will be the UAE flag colors which are red, green, white and black.
Updates
Project Deadline Extended
Reason: We need more designs and options.
Keep sending in more creative designs. thanks.
Industry/Entity Type
Business
Look and feel
Each slider illustrates characteristics of the customer's brand and the style your logo design should communicate.

```html
<!DOCTYPE html>
<html lang="en">
<head>
<meta charset="utf-8">
<title>Harbor Link Guild</title>
<link href="https://fonts.googleapis.com/css2?family=Source+Sans+3:wght@300;400;600&display=swap" rel="stylesheet">
<style>
:root{
  --red:#d9101f;
  --red-light:#e8243a;
  --green:#0e9a5c;
  --green-dark:#087a45;
  --ink:#2b2b2b;
  --text:#444;
  --muted:#777;
  --footer:#333;
  --white:#fff;
}
*{margin:0;padding:0;box-sizing:border-box}
html,body{width:1036px;height:1200px;overflow:hidden;background:var(--white)}
body{position:relative;font-family:"Source Sans 3",sans-serif;color:var(--text)}
.abs{position:absolute}

.brand{left:72px;top:40px;display:flex;align-items:center;gap:10px;font-size:25px;font-weight:600;color:var(--green-dark);letter-spacing:.5px}
.brand-dot{width:22px;height:22px;border-radius:50%;background:var(--red)}
.nav{left:414px;top:52px;display:flex;font-size:19px;font-weight:300;color:var(--ink)}
.nav a{color:inherit;text-decoration:none;padding:0 14px;border-left:1px solid #bbb;line-height:22px}
.nav a:first-child{padding-left:0;border-left:none}
.btn{top:46px;height:33px;border-radius:17px;color:var(--white);font-size:14px;display:flex;align-items:center;justify-content:center;box-shadow:0 1px 2px rgba(0,0,0,.3)}
.btn-login{left:819px;width:72px;background:linear-gradient(#17b56e,var(--green-dark))}
.btn-register{left:896px;width:72px;background:linear-gradient(#333,#000)}

.red-band{left:0;top:114px;width:1036px;height:329px;background:linear-gradient(var(--red-light),var(--red))}
.slider{left:68px;top:136px;width:900px;height:347px;background:var(--white);border-radius:14px 14px 0 0}
.slide{left:75px;top:142px;width:884px;height:334px;border-radius:10px;background:linear-gradient(100deg,#c9b79a 0%,#e9e4dc 35%,#f4f4f2 60%,#e6e8ea 100%)}
.arrow{top:275px}
.features{left:68px;top:483px;width:900px;height:129px;border-radius:0 0 14px 14px;background:linear-gradient(var(--green),var(--green-dark));display:flex;box-shadow:0 12px 14px -8px rgba(0,0,0,.25)}
.feature{flex:none;padding:26px 0 0 40px;color:var(--white)}
.feature+.feature{border-left:1px solid rgba(255,255,255,.25)}
.feature h3{font-size:20px;font-weight:400;margin-bottom:5px}
.feature p{font-size:12px;font-weight:300;line-height:18px;width:250px}

.welcome{left:68px;top:646px;width:560px}
h2{font-size:24px;font-weight:300;color:var(--ink);margin-bottom:8px}
.welcome p{font-size:12px;line-height:21px;font-weight:300;color:var(--ink);margin-bottom:7px}
.welcome p.muted{color:var(--muted)}
.mission{left:68px;top:845px;width:560px}
.mission h2{font-size:22px;margin-bottom:8px}
.mission ul{list-style:none}
.mission li{position:relative;padding-left:21px;font-size:12px;font-weight:300;line-height:21px;color:var(--ink);margin-bottom:4.5px}
.mission li svg{position:absolute;left:0;top:5px}

.how{left:664px;top:646px}
.how h2{color:var(--red)}
.video{left:664px;top:680px;width:298px;height:199px;border-radius:4px;background:linear-gradient(90deg,#e9ecef,#d3d6d9 50%,#c9ccd0)}
.play{left:785px;top:757px}
.cta{left:667px;top:891px;width:295px;height:125px;background:linear-gradient(var(--red-light),var(--red));border-radius:3px;padding:15px 0 0 27px;color:var(--white)}
.cta h3{font-size:23px;font-weight:600;line-height:28px;margin:0}
.cta p{font-size:12.5px;font-weight:400;line-height:17px;width:220px}
.cta-btn{position:absolute;left:29px;top:81px;width:101px;height:27px;background:#9c0c15;border-radius:2px;font-size:12px;display:flex;align-items:center;justify-content:center;gap:6px}

.footer{left:0;top:1096px;width:1036px;height:104px;background:linear-gradient(#404040,#2b2b2b)}
.foot-links{left:76px;top:1122px;font-size:13.5px;color:var(--white)}
.foot-links span{padding:0 6px;color:#ccc}
.copy{left:76px;top:1148px;font-size:11px;color:#bbb;font-weight:300}
.social{left:901px;top:1118px;display:flex;gap:4px}
.social i{width:20px;height:20px;border-radius:3px;background:#4a8fd0}
</style>
</head>
<body>
<header>
  <div class="abs brand"><span class="brand-dot"></span>Harbor Link Guild</div>
  <nav class="abs nav"><a>Home</a><a>Directory</a><a>Articles</a><a>Deals</a><a>Forums</a></nav>
  <div class="abs btn btn-login">Log In</div>
  <div class="abs btn btn-register">Register</div>
</header>

<div class="abs red-band"></div>
<div class="abs slider"></div>
<div class="abs slide" role="img" aria-label="Slider photo of business members meeting over coffee"></div>
<svg class="abs arrow" style="left:90px" width="32" height="66" viewBox="0 0 32 66"><polyline points="30,2 3,33 30,64" fill="none" stroke="#fff" stroke-width="2"/></svg>
<svg class="abs arrow" style="left:912px" width="32" height="66" viewBox="0 0 32 66"><polyline points="2,2 29,33 2,64" fill="none" stroke="#fff" stroke-width="2"/></svg>

<section class="abs features">
  <div class="feature" style="width:297px"><h3>Why Choose Us?</h3><p>Phasellus felis dolor, scelerisque a, tempus eget, lobortis id, libero. Donec scelerisque leo ac risus</p></div>
  <div class="feature" style="width:300px;padding-top:28px"><h3>What We Do</h3><p>Phasellus felis dolor, scelerisque a, tempus eget, lobortis id, libero. Donec scelerisque leo ac risus</p></div>
  <div class="feature" style="width:303px;padding-top:28px"><h3>How to Register?</h3><p>Phasellus felis dolor, scelerisque a, tempus eget, lobortis id, libero. Donec scelerisque leo ac risus</p></div>
</section>

<section class="abs welcome">
  <h2>Welcome to Harbor Link Guild Maipage</h2>
  <p>Vivamus porttitor, g, purus nisi eleifend libero, a tempus libero lectus feugiat felis. Morbi diam mauris, viverra in, gravida eu, mattis in, ante. Morbi eget arcu. Morbi porta, libero id ullamcorper</p>
  <p class="muted">Nonummy, nibh ligula pulvinar metus, eget consectetuer augue nisi quis lacus. Ut ac mi quis lacus mollis aliquam. Curabitur iaculis tempus eros. Curabitur vel mi sit amet magna malesuada ultrices. Ut nisi erat, fermentum vel, congue id, euismod in, elit. Fusce ultricies, orci ac feugiat suscipit, leo massa sodales velit, et scelerisque mi tortor at ipsum.</p>
</section>

<section class="abs mission">
  <h2>Our Mission &amp; Services</h2>
  <ul>
    <li><svg width="14" height="12" viewBox="0 0 14 12"><polyline points="1,6 5,10 13,1" fill="none" stroke="#666" stroke-width="2.5"/></svg>Harbor Link Guild will allow you to maximize the potential of your Harbor Link business.</li>
    <li><svg width="14" height="12" viewBox="0 0 14 12"><polyline points="1,6 5,10 13,1" fill="none" stroke="#666" stroke-width="2.5"/></svg>A business Networking Platform helping Harbor Link members' source new customers.</li>
    <li><svg width="14" height="12" viewBox="0 0 14 12"><polyline points="1,6 5,10 13,1" fill="none" stroke="#666" stroke-width="2.5"/></svg>Build mutual business relationships with fellow Harbor Link companies.</li>
    <li><svg width="14" height="12" viewBox="0 0 14 12"><polyline points="1,6 5,10 13,1" fill="none" stroke="#666" stroke-width="2.5"/></svg>The Harbor Link Guild keeps you up to date with what's happening and where.</li>
    <li><svg width="14" height="12" viewBox="0 0 14 12"><polyline points="1,6 5,10 13,1" fill="none" stroke="#666" stroke-width="2.5"/></svg>Provide a supportive infrastructure to enable companies to access and engage in unlimited networking opportunities.</li>
  </ul>
</section>

<div class="abs how"><h2>How it Works</h2></div>
<div class="abs video" role="img" aria-label="Video still of two colleagues reviewing a laptop"></div>
<svg class="abs play" width="42" height="42" viewBox="0 0 42 42"><circle cx="21" cy="21" r="21" fill="#fff" opacity=".9"/><polygon points="16,12 30,21 16,30" fill="#111"/></svg>

<aside class="abs cta">
  <h3>Why Register</h3>
  <p>Vivamus porttitor, g, purus nisi eleifend tempus libero lectus feugiat felis.</p>
  <div class="cta-btn">CLICK HERE <svg width="16" height="16" viewBox="0 0 16 16"><circle cx="8" cy="8" r="7" fill="none" stroke="#fff" stroke-width="1.6"/><path d="M4 8h7M8 5l3 3-3 3" fill="none" stroke="#fff" stroke-width="1.6"/></svg></div>
</aside>

<footer>
  <div class="abs footer"></div>
  <div class="abs foot-links">About HLG <span>|</span> Contact HGL <span>|</span> Terms &amp; conditions <span>|</span> privacy</div>
  <div class="abs copy">Copyright © 2013 Company Name. All rights reserved.</div>
  <div class="abs social"><i></i><i></i><i></i></div>
</footer>
</body>
</html>
```